Law firm business cards and stationary
Traditional professional presentation
Law firm business cards and stationary - Law
Creative Brief
Use same font as used in my logo
Other traditional looking fonts will be considered
Professional
Marla J. Pettigrew
Attorney at Law
742 E. 9th Ave, Ste 114 Spokane, WA 99208
(509) TRY-CASE
barrister@mailwove.com
roadcasedefenders.org
Please see uploaded logo. The phone number (509) TRY-CASE is displayed prominently in all marketing. Thank you.

```html
<!DOCTYPE html>
<html lang="en">
<head>
<meta charset="utf-8">
<title>The Calder Firm – Business Cards</title>
<link rel="stylesheet" href="https://fonts.googleapis.com/css2?family=Cinzel:wght@400;600&display=swap">
<style>
  :root {
    --page: #f1f2f0;
    --card-white: #ffffff;
    --green: #5bb531;
    --green-dark: #3a8a1c;
    --green-light: #a6dc70;
    --ink: #4a4a4a;
    --ink-soft: #6b6b6b;
    --shadow: rgba(0, 0, 0, 0.18);
  }
  * { box-sizing: border-box; margin: 0; padding: 0; }
  html, body { width: 1200px; height: 980px; overflow: hidden; }
  body {
    background: var(--page);
    position: relative;
    font-family: "Cinzel", "Times New Roman", serif;
  }
  .card {
    position: absolute;
    width: 640px;
    height: 366px;
    border-radius: 22px;
    overflow: hidden;
    box-shadow: 0 10px 28px var(--shadow);
  }

  /* Front */
  .card-front { left: 70px; top: 90px; background: var(--card-white); }
  .card-front .wave { position: absolute; inset: 0; width: 100%; height: 100%; }
  .firm-mark {
    position: absolute; left: 40px; top: 30px;
    display: flex; align-items: center; gap: 12px;
  }
  .firm-dot {
    width: 44px; height: 44px; border-radius: 50%;
    background: var(--green); flex: none;
  }
  .firm-name {
    font-size: 26px; font-weight: 600; color: var(--ink);
    letter-spacing: 1px; line-height: 1; white-space: nowrap;
  }
  .contact-list {
    position: absolute; left: 58px; top: 96px;
    list-style: none;
    display: flex; flex-direction: column; gap: 6px;
  }
  .contact-item {
    display: flex; align-items: center; gap: 10px;
    font-size: 12px; color: var(--ink-soft); letter-spacing: 0.6px;
    white-space: nowrap;
  }
  .contact-icon { width: 16px; height: 16px; flex: none; }
  .contact-item .address { line-height: 1.35; }
  .contact-phone {
    font-size: 18px; font-weight: 600; color: var(--green-dark); letter-spacing: 1px;
  }
  .contact-phone .contact-icon { width: 20px; height: 20px; }
  .holder {
    position: absolute; right: 40px; bottom: 30px;
    text-align: right; color: #fff;
  }
  .holder-name { font-size: 17px; letter-spacing: 1px; }
  .holder-title { font-size: 11px; letter-spacing: 1.5px; margin-top: 4px; }

  /* Back */
  .card-back {
    left: 490px; top: 530px;
    background: radial-gradient(ellipse at 50% 40%, var(--green-light) 0%, var(--green) 55%, var(--green-dark) 100%);
    display: flex; flex-direction: column; align-items: center; justify-content: center;
  }
  .back-name {
    font-size: 40px; font-weight: 600; color: #2f5f1c; letter-spacing: 2px;
  }
  .back-web {
    margin-top: 34px; font-size: 14px; letter-spacing: 3px;
    color: #ffffff; text-transform: uppercase;
  }
</style>
</head>
<body>

<section class="card card-front" aria-label="Business card front">
  <svg class="wave" viewBox="0 0 640 366" preserveAspectRatio="none" aria-hidden="true">
    <defs>
      <linearGradient id="waveFill" x1="0" y1="0" x2="1" y2="1">
        <stop offset="0" stop-color="#6cc23e"/>
        <stop offset="1" stop-color="#3f9221"/>
      </linearGradient>
    </defs>
    <path d="M0 254 C150 320 300 205 440 230 C530 246 590 254 640 240 L640 366 L0 366 Z" fill="url(#waveFill)"/>
    <path d="M0 238 C150 304 300 190 440 214 C530 230 590 238 640 224" fill="none" stroke="#a6dc70" stroke-width="5"/>
    <path d="M0 284 C160 350 330 250 470 268 C560 280 610 286 640 278" fill="none" stroke="#8ccf55" stroke-width="2" opacity="0.7"/>
  </svg>

  <div class="firm-mark">
    <span class="firm-dot"></span>
    <span class="firm-name">The Calder Firm</span>
  </div>

  <ul class="contact-list">
    <li class="contact-item">
      <svg class="contact-icon" viewBox="0 0 16 16" aria-hidden="true"><circle cx="8" cy="8" r="8" fill="#5bb531"/><path d="M8 3.5a2.6 2.6 0 0 0-2.6 2.6C5.4 8 8 12 8 12s2.6-4 2.6-5.9A2.6 2.6 0 0 0 8 3.5zm0 3.6a1 1 0 1 1 0-2 1 1 0 0 1 0 2z" fill="#fff"/></svg>
      <span class="address">742 E. 9th Ave, Ste 114<br>Spokane, WA 99208</span>
    </li>
    <li class="contact-item contact-phone">
      <svg class="contact-icon" viewBox="0 0 16 16" aria-hidden="true"><circle cx="8" cy="8" r="8" fill="#5bb531"/><path d="M5.3 4h1.6l.7 1.9-1 .8a5.5 5.5 0 0 0 2.7 2.7l.8-1 1.9.7v1.6c0 .4-.4.8-.8.8A7 7 0 0 1 4.5 4.8c0-.4.4-.8.8-.8z" fill="#fff"/></svg>
      <span>(509) TRY-CASE</span>
    </li>
    <li class="contact-item">
      <svg class="contact-icon" viewBox="0 0 16 16" aria-hidden="true"><circle cx="8" cy="8" r="8" fill="#5bb531"/><rect x="4" y="5" width="8" height="6" rx="0.8" fill="#fff"/><path d="M4.3 5.4 8 8.3l3.7-2.9" fill="none" stroke="#5bb531" stroke-width="0.9"/></svg>
      <span>barrister@mailwove.com</span>
    </li>
    <li class="contact-item">
      <svg class="contact-icon" viewBox="0 0 16 16" aria-hidden="true"><circle cx="8" cy="8" r="8" fill="#5bb531"/><circle cx="8" cy="8" r="4" fill="none" stroke="#fff" stroke-width="1"/><path d="M4 8h8M8 4c-1.6 1.8-1.6 6.2 0 8M8 4c1.6 1.8 1.6 6.2 0 8" fill="none" stroke="#fff" stroke-width="0.9"/></svg>
      <span>roadcasedefenders.org</span>
    </li>
  </ul>

  <div class="holder">
    <p class="holder-name">Marla J. Pettigrew</p>
    <p class="holder-title">Attorney at Law</p>
  </div>
</section>

<section class="card card-back" aria-label="Business card back">
  <p class="back-name">The Calder Firm</p>
  <p class="back-web">roadcasedefenders.org</p>
</section>

</body>
</html>
```